Überarbeitung/Optimierung eines edlen Layouts für eine Booklet-Seite
Zielgruppe
Diese Booklet-Seite (Vorder- und Rückseite) soll dem Leser übersichtliche Informationen über den Velmer Münster bieten.
Aufgabenstellung
Das bisherige Design (siehe Dateien) gefällt uns schon sehr. Trotzdem fragen wir uns, ob man es noch etwas professioneller gestalten kann? Insbesondere die Überschrift und die Zitate machen uns Sorgen.
Das grundlegende, schlichte Design soll beibehalten werden (weißer Hintergrund, Font 'Open Sans', keine/kaum Design-Elemente bis auf das Logo).
Die Seiten (21x21cm) wurden im Affinity Designer erstellt und sollen für verschiedene Themen (also nicht nur Velmer Münster) das grundlegende Layout vorgeben.

```html
<!DOCTYPE html>
<html lang="de">
<head>
<meta charset="utf-8">
<title>Velmer Münster – Booklet-Seite</title>
<link rel="stylesheet" href="https://fonts.googleapis.com/css2?family=Open+Sans:ital,wght@0,300;0,400;0,600;1,300&display=swap">
<style>
  :root {
    --paper: #ffffff;
    --ink: #1c1c1c;
    --ink-soft: #4a4a4a;
    --rule: #1c1c1c;
    --engraving-light: #e6e6e6;
    --engraving-dark: #8a8a8a;
    --sky-top: #6f86b0;
    --sky-mid: #d9a9a0;
    --city: #6b6460;
  }
  * { margin: 0; padding: 0; box-sizing: border-box; }
  html, body {
    width: 1200px; height: 1200px; overflow: hidden;
    background: var(--paper);
  }
  .page {
    position: relative; width: 1200px; height: 1200px;
    font-family: "Open Sans", Arial, sans-serif;
    color: var(--ink);
  }
  .hero-engraving {
    position: absolute; left: 45px; top: 45px; width: 938px; height: 345px;
    background: linear-gradient(180deg, var(--engraving-light) 0%, #bcbcbc 55%, var(--engraving-dark) 100%);
  }
  .brand {
    position: absolute; left: 1012px; top: 56px; width: 124px;
    display: flex; flex-direction: column; align-items: flex-start; gap: 10px;
  }
  .brand-square { width: 20px; height: 20px; border: 1.5px solid var(--ink); }
  .brand-name {
    font-size: 21px; line-height: 24px; font-weight: 400; letter-spacing: 0.5px;
    color: var(--ink);
  }
  .page-title {
    position: absolute; left: 45px; top: 404px; width: 938px;
    display: flex; align-items: baseline; gap: 18px;
  }
  .page-title h1 {
    font-size: 34px; line-height: 44px; font-weight: 600; letter-spacing: 0.3px;
  }
  .page-title .title-rule {
    flex: 1; height: 1px; background: var(--rule); transform: translateY(-10px);
  }
  .intro {
    position: absolute; left: 45px; top: 470px; width: 1103px;
    font-size: 20px; line-height: 27px; text-align: justify; hyphens: auto;
    color: var(--ink);
  }
  .quote {
    position: absolute; left: 45px; top: 726px; width: 612px;
    padding-left: 22px; border-left: 3px solid var(--rule);
  }
  .quote-text {
    font-size: 24px; line-height: 34px; font-weight: 300; font-style: italic;
    color: var(--ink);
  }
  .quote-source {
    margin-top: 12px;
    font-size: 16px; line-height: 24px; font-weight: 400; color: var(--ink-soft);
  }
  .quote-source .name { font-weight: 600; color: var(--ink); }
  .body-text {
    position: absolute; left: 45px; top: 918px; width: 615px;
    font-size: 20px; line-height: 29px; text-align: justify; hyphens: auto;
    color: var(--ink);
  }
  .city-photo {
    position: absolute; left: 686px; top: 687px; width: 459px; height: 458px;
    background: linear-gradient(180deg, var(--sky-top) 0%, var(--sky-mid) 35%, #9a8a86 55%, var(--city) 100%);
  }
</style>
</head>
<body>
<div class="page">
  <div class="hero-engraving" role="img" aria-label="Historischer Stich des Velmer Münsters während der Bauarbeiten im 19. Jahrhundert mit Baukran"></div>

  <div class="brand">
    <span class="brand-square"></span>
    <span class="brand-name">CHRONIK<br>HAUS</span>
  </div>

  <div class="page-title">
    <h1>Velmer Münster</h1>
    <span class="title-rule"></span>
  </div>

  <p class="intro">Bei der Wiederaufnahme der Bauarbeiten im 19. Jahrhundert wurde der Dom zum zentralen Zeichen der Einigkeit im Deutschen Bund und des Traums von einem zweiten deutschen Kaiserreich. Und auch heute noch wirkt das Velmer Wahrzeichen mit seiner ungeheuren Symbolkraft in der ganzen Welt. Seine große wirtschaftliche Bedeutung für die Stadt als Pilger- und Touristenmagnet ist seit dem Mitelalter ungebrochen. Aus der jüngeren Geschichte ist insbesondere das Bild von Velm in Trümmern präsent, aus denen der Dom zwar beschädigt, aber standhaft als unerschütterliches Wahrzeichen der Stadt herausragt.</p>

  <blockquote class="quote">
    <p class="quote-text">„Der Erhalt des Velmer Münsters wird als Aufgabe ewig bleiben.“</p>
    <p class="quote-source"><span class="name">Matthias K.R. Lindner</span>, Präsident des Dombauvereins</p>
  </blockquote>

  <p class="body-text">Im Jahr 2008 wurde durch Kernbohrungen ein Durchbruch durch die bis zu elf Meter dicken Außenmauern des Südturm-Fundaments geschaffen, um einen neuen Zugang zum Turmaufstieg zu ermöglichen. Der Verein kümmert sich seit über 175 Jahren um den Erhalt des Velmer Münsters und leistet mit seinen über 17.000 Mitgliedern einen wesentlichen Beitrag zum Erhalt dieses großartigen Gebäudes.</p>

  <div class="city-photo" role="img" aria-label="Foto der Stadt Velm in der Abenddämmerung mit den Doppeltürmen des Münsters, Fernsehturm und Bogenbrücke"></div>
</div>
</body>
</html>
```